Global social media analytics company needs business card design

We need an updated business card design to align with our new website - brightquillo.net -

I would also like a favicon designed as well.

Target Market(s)

CEOs, CMOs go big companies

Industry/Entity Type

Business

Contact Information for Business Card

Room for the following:
Address
Main telephone
Direct telephone or cell phone
twitter handle

Colors
aaaaaa

Requirements
Must have
• Attention to detail; style.
• Use the logo color from our website - which is gray

```html
<!DOCTYPE html>
<html lang="en">
<head>
<meta charset="utf-8">
<title>brightquillo stationery</title>
<link rel="stylesheet" href="https://fonts.googleapis.com/css2?family=Open+Sans:wght@400;600;700&display=swap">
<style>
:root{
  --backdrop:#c9c9c9;
  --paper:#ffffff;
  --brand-gray:#4a4a4a;
  --accent:#f7a81e;
  --text:#333333;
  --muted:#666666;
  --rule:#9a9a9a;
  --stamp:#8a78b8;
}
*{margin:0;padding:0;box-sizing:border-box}
html,body{width:1029px;height:1200px;overflow:hidden}
body{background:var(--backdrop);font-family:"Open Sans",Arial,sans-serif;color:var(--text);position:relative}
.sheet{position:absolute;background:var(--paper);box-shadow:0 6px 18px rgba(0,0,0,.18)}
.letterhead{left:80px;top:43px;width:556px;height:720px}
.envelope{left:204px;top:847px;width:622px;height:272px}
.card-front{left:722px;top:436px;width:229px;height:131px;background:var(--accent)}
.card-back{left:723px;top:630px;width:229px;height:133px}
.band{position:absolute;left:0;right:0;bottom:0;background:var(--accent)}
.letterhead .band{height:20px}
.envelope .band{height:4px;bottom:12px}

.logo{position:absolute;display:flex;flex-direction:column;align-items:center}
.logo-mark{border-radius:50%;background:var(--brand-gray)}
.logo-name{font-weight:700;color:var(--brand-gray);letter-spacing:-.3px;line-height:1}
.letterhead .logo{left:44px;top:23px}
.letterhead .logo-mark{width:56px;height:56px;margin-bottom:7px}
.letterhead .logo-name{font-size:16px}
.envelope .logo{left:30px;top:26px}
.envelope .logo-mark{width:58px;height:58px;margin-bottom:8px}
.envelope .logo-name{font-size:17px}
.card-front .logo{left:0;right:0;top:28px}
.card-front .logo-mark{width:50px;height:50px;background:var(--paper);margin-bottom:8px}
.card-front .logo-name{font-size:15px;color:var(--paper)}
.card-back .logo{left:10px;top:9px;flex-direction:row;gap:4px}
.card-back .logo-mark{width:20px;height:20px}
.card-back .logo-name{font-size:10px}

.contacts{position:absolute;display:grid;grid-template-columns:auto auto;column-gap:14px;row-gap:5px;font-size:6.6px;color:var(--text);line-height:1.3}
.contact{display:flex;align-items:flex-start;gap:7px}
.contact svg{flex:none}
.letterhead .contacts{left:294px;top:62px;column-gap:12px}
.envelope .contacts{left:392px;top:36px;font-size:7px;column-gap:22px}
.card-back .contacts{left:14px;top:92px;font-size:5.4px;column-gap:26px;row-gap:4px}
.card-back .contact{gap:6px}

.meta{position:absolute;left:51px;top:149px;display:flex;gap:75px;font-size:6.4px;line-height:1.35}
.meta .label{color:var(--muted)}
.rule{position:absolute;left:51px;width:460px;top:185px;height:1px;background:var(--rule)}
.body-copy{position:absolute;left:53px;top:211px;width:460px;font-size:6.5px;line-height:12px;color:var(--text)}
.body-copy p{margin-bottom:12px}
.signature{position:absolute;left:305px;top:580px;width:95px;height:55px;background:linear-gradient(90deg,#e6e6e6,#f4f4f4);border-radius:4px}
.stamp{position:absolute;left:390px;top:568px;width:92px;height:92px;border-radius:50%;border:3px solid var(--stamp);opacity:.85}

.person{position:absolute;right:16px;top:44px;text-align:right}
.person-name{font-size:12px;color:var(--text);line-height:1.2}
.person-role{font-size:6.4px;color:var(--accent)}
</style>
</head>
<body>
<svg width="0" height="0" style="position:absolute">
  <defs>
    <symbol id="i-phone" viewBox="0 0 20 20"><circle cx="10" cy="10" r="10" fill="#f7a81e"/><path d="M6.5 5.5l2 0 1 2.5-1.3 1a6 6 0 0 0 2.8 2.8l1-1.3 2.5 1v2c0 .6-.5 1-1 1A8 8 0 0 1 5.5 6.5c0-.5.4-1 1-1z" fill="#fff"/></symbol>
    <symbol id="i-mail" viewBox="0 0 20 20"><circle cx="10" cy="10" r="10" fill="#f7a81e"/><rect x="5" y="6.5" width="10" height="7" rx="1" fill="#fff"/><path d="M5.5 7l4.5 3.5L14.5 7" stroke="#f7a81e" stroke-width="1" fill="none"/></symbol>
    <symbol id="i-web" viewBox="0 0 20 20"><circle cx="10" cy="10" r="10" fill="#f7a81e"/><circle cx="10" cy="10" r="5" fill="none" stroke="#fff" stroke-width="1.3"/><path d="M5 10h10M10 5c-2.5 3-2.5 7 0 10M10 5c2.5 3 2.5 7 0 10" stroke="#fff" stroke-width="1" fill="none"/></symbol>
    <symbol id="i-pin" viewBox="0 0 20 20"><circle cx="10" cy="10" r="10" fill="#f7a81e"/><path d="M10 15.5s-4-4-4-7a4 4 0 0 1 8 0c0 3-4 7-4 7z" fill="#fff"/><circle cx="10" cy="8.5" r="1.5" fill="#f7a81e"/></symbol>
  </defs>
</svg>

<section class="sheet letterhead">
  <div class="logo"><div class="logo-mark"></div><div class="logo-name">brightquillo</div></div>
  <div class="contacts">
    <div class="contact"><svg width="12" height="12"><use href="#i-phone"/></svg>+1 555 014 2290</div>
    <div class="contact"><svg width="12" height="12"><use href="#i-web"/></svg>www.brightquillo.net</div>
    <div class="contact"><svg width="12" height="12"><use href="#i-mail"/></svg>info@brightquillo.net</div>
    <div class="contact"><svg width="12" height="12"><use href="#i-pin"/></svg>820 Harbor Lane,<br>3rd Fl Easton, MA 02375 USA</div>
  </div>
  <div class="meta">
    <div><div class="label">Date:</div>06/02/2015</div>
    <div><div class="label">Subject:</div>Lorem ipsum dolor sit amet, consectetur adipisicing elit.</div>
  </div>
  <div class="rule"></div>
  <div class="body-copy">
    <p>Lorem ipsum dolor sit amet, consectetur adipisicing elit, sed do eiusmod tempor incididunt ut labore et dolore magna aliqua. Ut enim ad minim veniam, quis nostrud exercitation ullamco laboris nisi ut aliquip ex ea commodo consequat. Duis aute irure dolor in reprehenderit in voluptate velit esse cillum dolore eu fugiat nulla pariatur.</p>
    <p>Excepteur sint occaecat cupidatat non proident, sunt in culpa qui officia deserunt mollit anim id est laborum. Lorem ipsum dolor sit amet, consectetur adipisicing elit, sed do eiusmod tempor incididunt ut labore et dolore magna aliqua. Ut enim ad minim veniam, quis nostrud exercitation ullamco laboris nisi ut aliquip ex ea commodo consequat.</p>
    <p>Duis aute irure dolor in reprehenderit in voluptate velit esse cillum dolore eu fugiat nulla pariatur. Excepteur sint occaecat cupidatat non proident, sunt in culpa qui officia deserunt mollit anim id est laborum.</p>
    <p>Lorem ipsum dolor sit amet, consectetur adipisicing elit, sed do eiusmod tempor incididunt ut labore et dolore magna aliqua. Ut enim ad minim veniam, quis nostrud exercitation ullamco laboris nisi ut aliquip ex ea commodo consequat. Duis aute irure dolor in reprehenderit in voluptate velit esse cillum dolore eu fugiat nulla pariatur. Excepteur sint occaecat cupidatat non proident, sunt in culpa qui officia deserunt mollit anim id est laborum.</p>
    <p>Lorem ipsum dolor sit amet, consectetur adipisicing elit, sed do eiusmod tempor incididunt ut labore et dolore magna aliqua. Ut enim ad minim veniam, quis nostrud exercitation ullamco laboris nisi ut aliquip ex ea commodo consequat. Duis aute irure dolor in reprehenderit in voluptate velit esse cillum dolore eu fugiat nulla pariatur. Excepteur sint occaecat cupidatat non proident, sunt in culpa qui officia deserunt mollit anim id est laborum.</p>
    <p>Excepteur sint occaecat cupidatat non proident, sunt in culpa qui officia deserunt mollit anim id est laborum. Lorem ipsum dolor sit amet, consectetur adipisicing elit, sed do eiusmod tempor incididunt ut labore et dolore magna aliqua. Ut enim ad minim veniam, quis nostrud exercitation ullamco laboris nisi ut aliquip ex ea commodo consequat.</p>
    <p>Duis aute irure dolor in reprehenderit in voluptate velit esse cillum dolore eu fugiat nulla pariatur. Excepteur sint occaecat cupidatat non proident, sunt in culpa qui officia deserunt mollit anim id est laborum.</p>
  </div>
  <div class="signature" role="img" aria-label="Handwritten signature"></div>
  <div class="stamp" role="img" aria-label="Company seal"></div>
  <div class="band"></div>
</section>

<section class="sheet card-front">
  <div class="logo"><div class="logo-mark"></div><div class="logo-name">brightquillo</div></div>
</section>

<section class="sheet card-back">
  <div class="logo"><div class="logo-mark"></div><div class="logo-name">brightquillo</div></div>
  <div class="person">
    <div class="person-name">Martin Kessler</div>
    <div class="person-role">Founder &amp; CEO</div>
  </div>
  <div class="contacts">
    <div class="contact"><svg width="11" height="11"><use href="#i-phone"/></svg>+1 555 014 2290</div>
    <div class="contact"><svg width="11" height="11"><use href="#i-web"/></svg>www.brightquillo.net</div>
    <div class="contact"><svg width="11" height="11"><use href="#i-mail"/></svg>info@brightquillo.net</div>
    <div class="contact"><svg width="11" height="11"><use href="#i-pin"/></svg>820 Harbor Lane,<br>3rd Fl Easton, MA 02375 USA</div>
  </div>
</section>

<section class="sheet envelope">
  <div class="logo"><div class="logo-mark"></div><div class="logo-name">brightquillo</div></div>
  <div class="contacts">
    <div class="contact"><svg width="13" height="13"><use href="#i-phone"/></svg>+1 555 014 2290</div>
    <div class="contact"><svg width="13" height="13"><use href="#i-web"/></svg>www.brightquillo.net</div>
    <div class="contact"><svg width="13" height="13"><use href="#i-mail"/></svg>info@brightquillo.net</div>
    <div class="contact"><svg width="13" height="13"><use href="#i-pin"/></svg>820 Harbor Lane,<br>3rd Fl Easton, MA 02375 USA</div>
  </div>
  <div class="band"></div>
</section>
</body>
</html>
```